Revamp our software development company Wix site

We need to rework our Wix website theming, layout, design to match our logo file color and theming. There are a few elements we want to keep, such as the top splash 'typing' header.

The current site is hiketoucan.net. This website I created with Wix, but I never fully finished the copy and all sections.

The feel and mood of the site should be "Warm, professional, inviting, and should project expertise in the field, confidence." But not corporate and cold.

The colors and fonts should match the logo theming. The website must match the logo which was designed in a separate contest. So browns, greens, whites, etc. to create a warm and professional, but fun website.

I want to showcase our app development screenshots in a nice, sharp way.

We are a new company, with only a few clients and projects under our belt. So we don't have lots of need for many testimonials, project showcases, etc. just a couple which is why we went with "Recent work" instead of "Portfolio".

It needs a blog section also that looks great, and will allow me to manage the blog after this project is over. The blog's purpose is for SEO content and marketing.

It will be a huge win for the makerbazaar artist, to make something unique that doesn't look like every other templated website.

We can use the text/sections found on hiketoucan.net, then i would like to tweak some of the copy and sections later.

***This is a Wix website*** I think it would be 2 pages. The landing page, then the blog page.

***Awesome inspiration websites/vibes we like***
https://ninekitesworks.com/
https://vostrella.com/
https://www.larkspinmedia.com/
https://www.triplumeworks.com/
https://harbor-makerhaus.com/
https://frostquill.works/

If you have ideas that need to break free from Wix environment, I am open to that idea also. Wix is just easy for a non-technical founder like me to manage our site/blog.

Thanks!

Target Market(s)

Industry leading commercial and residential construction companies seeking custom software development

Industry/Entity Type

We are a boutique software development studio.

Coding

Coded - Design and coding required

Font styles to use
Sans Serif

Requirements
Must have
• Darker/warm background and overall feel. Relaxed and confident vibes. Simplicity, less is more approach. Blog page. Must have project gallery to showcase high res- screenshots. Clear sans serif fonts, nice contrasting colors.
Nice to have
• If it could have some sort of construction related flare, like photos or icon, that could be good, but it cannot be cheesy. A lot of the stock photos of construction workers etc. are terrible and cheesy (please do not use).
Should not have
• lots of pages, music/sounds, busy theming, tiny fonts

```html
<!DOCTYPE html>
<html lang="en">
<head>
<meta charset="utf-8">
<title>Toucan Studio — Custom Software for Builders</title>
<link href="https://fonts.googleapis.com/css2?family=Montserrat:wght@400;500;600;700&family=DM+Serif+Display:ital@1&display=swap" rel="stylesheet">
<style>
:root{
  --ink:#111111;
  --text:#222222;
  --muted:#666666;
  --lime:#b5d22a;
  --footer:#2f2f2b;
  --white:#ffffff;
}
*{box-sizing:border-box;margin:0;padding:0}
html,body{width:1200px;height:4766px;overflow:hidden}
body{position:relative;font-family:'Montserrat',sans-serif;color:var(--text);background:var(--white)}
.abs{position:absolute}
/* hero */
.hero{position:absolute;left:0;top:0;width:1200px;height:614px;background:var(--ink);overflow:hidden}
.hero-bg{position:absolute;inset:0;background:linear-gradient(180deg,#0e0e0e 0%,#1d1d1d 55%,#141414 100%)}
.hero-haze{position:absolute;left:380px;top:60px;width:420px;height:554px;background:linear-gradient(180deg,rgba(255,255,255,.05),rgba(255,255,255,.02));}
.brand{position:absolute;display:flex;align-items:center;gap:10px;font-weight:700;color:var(--white)}
.brand-dot{width:34px;height:34px;border-radius:50%;background:var(--lime)}
.brand-name{font-size:38px;letter-spacing:-.5px}
.nav{position:absolute;top:31px;left:583px;display:flex;align-items:center;font-size:13px;color:var(--white)}
.nav a{color:var(--white);text-decoration:none}
.nav .active{color:var(--lime)}
.btn-outline{border:1.5px solid var(--lime);border-radius:18px;padding:9px 18px;font-size:12px}
.call{display:flex;align-items:center;gap:10px}
.call-icon{width:38px;height:38px;border-radius:50%;background:var(--lime);display:flex;align-items:center;justify-content:center}
.call small{display:block;font-size:11px}
.call strong{font-size:19px;letter-spacing:.5px}
.hero-title{position:absolute;left:107px;top:196px;color:var(--white);font-weight:600;font-size:56px;line-height:88px}
.hero-title em{font-family:'DM Serif Display',serif;font-style:italic;font-weight:400;color:var(--lime);font-size:70px}
.hero-disc{position:absolute;left:720px;top:130px;width:400px;height:400px;border-radius:50%;background:var(--lime)}
.hero-disc-cut{position:absolute;left:790px;top:200px;width:260px;height:260px;border-radius:50%;background:#1a1a1a}
.hero-photo{position:absolute;left:760px;top:96px;width:340px;height:518px;border-radius:170px 170px 0 0;background:linear-gradient(180deg,#e9e4de 0%,#f4f4f2 34%,#dedede 60%,#8d8d8d 84%,#5e5e5e 100%);box-shadow:0 20px 60px rgba(0,0,0,.45)}
.scroll-arrow{position:absolute;left:592px;top:560px}
/* intro */
.intro-title{position:absolute;left:0;top:678px;width:1200px;text-align:center;font-size:23px;font-weight:600;line-height:43px;color:var(--ink)}
.step{position:absolute;top:820px;width:250px;text-align:center}
.step-icon{position:relative;width:84px;height:84px;margin:0 auto;border-radius:50%;background:var(--lime);display:flex;align-items:center;justify-content:center}
.step-num{position:absolute;left:-4px;top:-2px;width:26px;height:26px;border-radius:50%;background:var(--ink);color:var(--white);font-size:11px;display:flex;align-items:center;justify-content:center}
.step h3{font-size:16px;font-weight:600;margin:18px 0 10px;color:var(--ink)}
.step p{font-size:11.5px;line-height:20px;color:var(--muted)}
/* feature rows */
.feature-img{position:absolute;width:343px;height:250px;border-radius:14px;overflow:hidden;box-shadow:0 10px 26px rgba(0,0,0,.14)}
.feature-text{position:absolute;width:420px}
.feature-text h2{font-size:23px;font-weight:600;color:var(--ink);margin-bottom:22px}
.feature-text p{font-size:12.5px;line-height:23px;color:#333}
/* recent work */
.work{position:absolute;left:0;top:2108px;width:1200px;height:580px;background:linear-gradient(120deg,#0b161d 0%,#123039 45%,#0b1b22 100%);overflow:hidden}
.work h2{position:absolute;left:0;top:48px;width:1200px;text-align:center;color:var(--white);font-size:24px;font-weight:600}
.shot{position:absolute;height:196px;border-radius:12px;padding:14px 18px;box-shadow:0 12px 30px rgba(0,0,0,.35)}
.screen{width:100%;height:100%;border-radius:6px;border:5px solid #1b1b1b}
/* testimonials */
.section-title{position:absolute;left:0;width:1200px;text-align:center;font-size:24px;font-weight:600;color:var(--ink)}
.quote{position:absolute;top:2838px;width:226px;height:270px;background:var(--white);border-radius:6px;box-shadow:0 4px 18px rgba(0,0,0,.08);text-align:center;padding:22px 18px}
.quote p{font-size:11.5px;line-height:20px;color:var(--muted);height:60px}
.stars{color:#f4b63f;font-size:16px;letter-spacing:4px;margin:12px 0 14px}
.avatar{width:72px;height:72px;border-radius:50%;margin:0 auto 12px;background:linear-gradient(160deg,#d9cfc6,#8a7f76);border:3px solid #eee}
.quote h4{font-size:14px;font-weight:600;color:var(--ink)}
.quote span{font-size:11px;letter-spacing:1px;color:var(--muted)}
.faded{opacity:.35}
.slider-btn{position:absolute;top:2980px;width:44px;height:44px;border-radius:50%;background:var(--lime);display:flex;align-items:center;justify-content:center;box-shadow:0 0 0 8px rgba(255,255,255,.85)}
/* blog */
.blog-sub{position:absolute;left:0;top:3240px;width:1200px;text-align:center;font-size:12.5px;line-height:23px;color:#333}
.post{position:absolute;top:3322px;width:291px}
.post-img{position:relative;height:180px;border-radius:4px}
.tag{position:absolute;left:8px;bottom:8px;background:var(--lime);color:var(--ink);font-size:11px;padding:4px 10px;border-radius:3px}
.post h3{font-size:13.5px;font-weight:600;line-height:25px;margin-top:14px;color:var(--ink)}
.meta{display:flex;gap:22px;font-size:12px;color:#333;margin-top:14px}
.meta span{display:flex;align-items:center;gap:6px}
.btn-fill{position:absolute;background:var(--lime);color:var(--ink);font-weight:600;font-size:11.5px;display:flex;align-items:center;justify-content:center;border-radius:4px;letter-spacing:.5px}
/* clients */
.client{position:absolute;top:3876px;display:flex;align-items:center;gap:10px;font-size:22px;font-weight:500;color:#555;letter-spacing:1px}
.client i{display:block;width:26px;height:26px;background:#555;border-radius:4px}
/* contact */
.contact{position:absolute;left:140px;top:4044px;width:918px;height:322px;background:var(--lime);border-radius:20px}
.contact h2{position:absolute;left:0;top:52px;width:100%;text-align:center;font-size:25px;font-weight:600;color:var(--ink)}
.contact p{position:absolute;left:0;top:101px;width:100%;text-align:center;font-size:12px;color:var(--ink)}
.field{position:absolute;width:384px;height:36px;background:var(--white);border-radius:4px;font-size:11px;color:#888;padding:11px 14px}
.submit{position:absolute;left:415px;top:264px;width:90px;height:32px;background:var(--ink);color:var(--white);font-size:11px;font-weight:600;border-radius:4px;display:flex;align-items:center;justify-content:center;letter-spacing:.5px}
/* footer */
.footer{position:absolute;left:0;top:4451px;width:1200px;height:315px;background:var(--footer);color:#e8e8e8}
.socials{position:absolute;left:185px;top:163px;display:flex;gap:10px}
.socials i{display:block;width:26px;height:26px;border-radius:50%;background:var(--lime)}
.fcol{position:absolute;top:75px;font-size:13px;line-height:28px}
.fcol h4{color:var(--lime);font-weight:500;font-size:14px;margin-bottom:8px}
.fcontact{display:flex;gap:10px;align-items:flex-start;line-height:20px;margin-bottom:12px}
.copyright{position:absolute;left:140px;top:262px;width:918px;border-top:1px solid #55554f;padding-top:20px;text-align:center;font-size:12px}
</style>
</head>
<body>

<header class="hero">
  <div class="hero-bg" role="img" aria-label="Dim construction site with cranes behind the headline"></div>
  <div class="hero-haze"></div>
  <div class="brand" style="left:105px;top:20px"><span class="brand-dot"></span><span class="brand-name">Toucan</span></div>
  <nav class="nav">
    <a class="active" href="#">Home</a>
    <a href="#" style="margin-left:80px">Blog</a>
    <a class="btn-outline" href="#" style="margin-left:62px">Contact Us</a>
    <div class="call" style="margin-left:30px">
      <span class="call-icon"><svg width="18" height="18" viewBox="0 0 24 24"><path fill="#111" d="M6.6 10.8a15 15 0 0 0 6.6 6.6l2.2-2.2c.3-.3.7-.4 1-.2 1.1.4 2.3.6 3.6.6.6 0 1 .4 1 1V20c0 .6-.4 1-1 1A17 17 0 0 1 3 4c0-.6.4-1 1-1h3.5c.6 0 1 .4 1 1 0 1.3.2 2.5.6 3.6.1.3 0 .7-.2 1z"/></svg></span>
      <div><small>Call Us Now</small><strong>555-014-2290</strong></div>
    </div>
  </nav>
  <h1 class="hero-title">Take your<br><em>client experience</em><br>to the next level</h1>
  <div class="hero-disc"></div>
  <div class="hero-disc-cut"></div>
  <div class="hero-photo" role="img" aria-label="Smiling developer in a white shirt holding a laptop"></div>
  <svg class="scroll-arrow" width="16" height="26" viewBox="0 0 16 26"><path d="M8 0v24M2 18l6 6 6-6" stroke="#aaa" stroke-width="1.5" fill="none"/></svg>
</header>

<h2 class="intro-title">We help leading builders break free from<br>off-the-shelf software.</h2>
<svg class="abs" style="left:330px;top:830px" width="540" height="60" viewBox="0 0 540 60"><path d="M0 30 C60 -10 120 70 200 30 M340 30 C400 -10 460 70 540 30" stroke="#333" stroke-width="1.5" stroke-dasharray="3 4" fill="none"/></svg>
<div class="step" style="left:160px"><div class="step-icon"><span class="step-num">01</span><svg width="40" height="40" viewBox="0 0 40 40"><rect x="5" y="8" width="30" height="22" rx="2" fill="none" stroke="#111" stroke-width="2"/><circle cx="20" cy="19" r="5" fill="none" stroke="#111" stroke-width="2"/><path d="M14 34h12" stroke="#111" stroke-width="2"/></svg></div><h3>Tailor</h3><p>Research shows that less than 10% of software features are frequently used, leaving many bells and whistles unclicked. We'll tailor to fit and eliminate this waste.</p></div>
<div class="step" style="left:475px"><div class="step-icon"><span class="step-num">02</span><svg width="40" height="40" viewBox="0 0 40 40"><circle cx="20" cy="12" r="5" fill="none" stroke="#111" stroke-width="2"/><path d="M8 34v-8l6-6h12l6 6v8" fill="none" stroke="#111" stroke-width="2"/></svg></div><h3>Empower</h3><p>When your team has tailored tools, they'll work happier, faster, and more effectively towards your goal KPI's.</p></div>
<div class="step" style="left:788px"><div class="step-icon"><span class="step-num">03</span><svg width="40" height="40" viewBox="0 0 40 40"><circle cx="16" cy="18" r="8" fill="none" stroke="#111" stroke-width="2"/><circle cx="28" cy="26" r="6" fill="none" stroke="#111" stroke-width="2"/><path d="M10 34h20" stroke="#111" stroke-width="2"/></svg></div><h3>Outcompete</h3><p>Deliver results faster, gain performance insights, and leave a lasting impression on clients.</p></div>

<div class="feature-img" style="left:140px;top:1130px;background:linear-gradient(180deg,#5d7180 0%,#9a8f88 30%,#e0a070 48%,#5a4a44 62%,#262a30 100%)" role="img" aria-label="Tower cranes over a city at sunset"></div>
<div class="feature-text" style="left:565px;top:1162px"><h2>Our Story</h2><p>At Toucan, we believe that technology can help businesses achieve more. That's why we've dedicated ourselves to creating software that truly empowers our clients. Our team is made up of experienced developers and business professionals who understand what it takes to succeed in today's competitive landscape.</p></div>

<div class="feature-text" style="left:140px;top:1508px"><h2>Our Vision</h2><p>Our vision is to help businesses of all sizes reach their full potential. We believe that by providing powerful, user-friendly software, we can help businesses become more efficient, more effective, and more successful.</p></div>
<div class="feature-img" style="left:652px;top:1452px;background:linear-gradient(180deg,#2a6fc0 0%,#86b5e2 40%,#9aa7a8 54%,#5f8a3a 64%,#4e8f28 100%)" role="img" aria-label="Green lawn in front of buildings under construction"></div>

<div class="feature-img" style="left:140px;top:1774px;background:linear-gradient(180deg,#6fa6d8 0%,#bcd3e6 50%,#a9a49a 72%,#6e6a62 100%)" role="img" aria-label="Bridge tower and cranes at a construction site"></div>
<div class="feature-text" style="left:565px;top:1816px"><h2>Our Software</h2><p>Our software is designed to be easy to use and highly effective. We've spent years developing and refining our technology to ensure that it meets the needs of businesses like yours. Whether you're looking to streamline your processes, improve client satisfaction, or boost your bottom line, our software can help.</p></div>

<section class="work" role="img" aria-label="Dark code background with project screenshots shown on devices">
  <h2>Our Recent Work</h2>
  <div class="shot" style="left:-10px;top:122px;width:88px;background:#e8edf2"><div class="screen" style="background:linear-gradient(#3b5a78,#dfe7ee)"></div></div>
  <div class="shot" style="left:98px;top:122px;width:290px;background:#eef3f8"><div class="screen" style="background:linear-gradient(180deg,#2f6fe0 0%,#2f6fe0 30%,#ffffff 30%,#f1f5fb 100%)"></div></div>
  <div class="shot" style="left:409px;top:122px;width:290px;background:#8a5b3a"><div class="screen" style="background:linear-gradient(135deg,#1d3a66,#2f5fa8)"></div></div>
  <div class="shot" style="left:719px;top:122px;width:291px;background:#e7ec2a"><div class="screen" style="background:linear-gradient(135deg,#132452,#2a4a8a)"></div></div>
  <div class="shot" style="left:1030px;top:122px;width:190px;background:#9fe0cf"><div class="screen" style="background:#f7faf9"></div></div>
  <div class="shot" style="left:-10px;top:340px;width:293px;background:#f2f2f2"><div class="screen" style="background:linear-gradient(135deg,#4a5f7e,#c9d2de)"></div></div>
  <div class="shot" style="left:303px;top:340px;width:290px;background:#f7a23a"><div class="screen" style="background:linear-gradient(135deg,#f25a6a,#f7a23a)"></div></div>
  <div class="shot" style="left:614px;top:340px;width:290px;background:#eeeeee"><div class="screen" style="background:linear-gradient(135deg,#4a2fd0,#c03ad6 60%,#f0a0d0)"></div></div>
  <div class="shot" style="left:924px;top:340px;width:290px;background:#7a5a3e"><div class="screen" style="background:linear-gradient(180deg,#ffffff 0%,#ffffff 60%,#2f9a5a 60%,#e8f2ec 100%)"></div></div>
</section>

<h2 class="section-title" style="top:2772px">Our Happy Customer</h2>
<div class="quote faded" style="left:-10px"><p>established fact that a reader distracted by the content of a page</p><div class="stars">★★★★★</div><div class="avatar" role="img" aria-label="Customer portrait"></div><h4>Lee Marsh</h4><span>CUSTOMER</span></div>
<div class="quote" style="left:237px"><p>It is a long established fact that a reader will be distracted by the readable content of a page</p><div class="stars">★★★★★</div><div class="avatar" role="img" aria-label="Customer portrait"></div><h4>Dale Morrow</h4><span>CUSTOMER</span></div>
<div class="quote" style="left:487px"><p>The point of using Lorem Ipsum is that it has a more-or-less normal distribution of letters</p><div class="stars">★★★★★</div><div class="avatar" role="img" aria-label="Customer portrait"></div><h4>Owen Fisk</h4><span>CUSTOMER</span></div>
<div class="quote" style="left:736px"><p>Contrary to popular belief, Lorem Ipsum is not simply random text. It has roots in a piece of classical</p><div class="stars">★★★★★</div><div class="avatar" role="img" aria-label="Customer portrait"></div><h4>Nadia Brell</h4><span>CUSTOMER</span></div>
<div class="quote faded" style="left:985px"><p>There are many variations of passages of text available, but the</p><div class="stars">★★★★★</div><div class="avatar" role="img" aria-label="Customer portrait"></div><h4>Reid Calvo</h4><span>CUSTOMER</span></div>
<div class="slider-btn" style="left:76px"><svg width="12" height="12" viewBox="0 0 12 12"><path d="M8 1L3 6l5 5" stroke="#fff" stroke-width="2" fill="none"/></svg></div>
<div class="slider-btn" style="left:1078px"><svg width="12" height="12" viewBox="0 0 12 12"><path d="M4 1l5 5-5 5" stroke="#fff" stroke-width="2" fill="none"/></svg></div>

<h2 class="section-title" style="top:3192px">Our Latest Blog</h2>
<p class="blog-sub">Get to know us by reading our latest insights, company updates, and<br>client success stories.</p>
<article class="post" style="left:140px"><div class="post-img" style="background:linear-gradient(135deg,#2e333d,#6a5a4e 50%,#c9b49a)" role="img" aria-label="Team collaborating at a computer"><span class="tag">Design</span></div><h3>Your company might be in need of a social media audit</h3><div class="meta"><span><svg width="13" height="13" viewBox="0 0 14 14"><circle cx="7" cy="4.5" r="3" fill="none" stroke="#333" stroke-width="1.2"/><path d="M1.5 13c0-3 2.5-5 5.5-5s5.5 2 5.5 5" fill="none" stroke="#333" stroke-width="1.2"/></svg>by admin</span><span><svg width="13" height="13" viewBox="0 0 14 14"><rect x="1" y="2" width="12" height="11" rx="1" fill="none" stroke="#333" stroke-width="1.2"/><path d="M1 5.5h12M4 0.5v3M10 0.5v3" stroke="#333" stroke-width="1.2"/></svg>1 Jan, 2024</span></div></article>
<article class="post" style="left:453px"><div class="post-img" style="background:linear-gradient(135deg,#f0f0f0,#b8c0ca 55%,#5d6a7a)" role="img" aria-label="Hands typing code on a laptop"><span class="tag">Development</span></div><h3>How can business utilize email marketing to nature</h3><div class="meta"><span><svg width="13" height="13" viewBox="0 0 14 14"><circle cx="7" cy="4.5" r="3" fill="none" stroke="#333" stroke-width="1.2"/><path d="M1.5 13c0-3 2.5-5 5.5-5s5.5 2 5.5 5" fill="none" stroke="#333" stroke-width="1.2"/></svg>by admin</span><span><svg width="13" height="13" viewBox="0 0 14 14"><rect x="1" y="2" width="12" height="11" rx="1" fill="none" stroke="#333" stroke-width="1.2"/><path d="M1 5.5h12M4 0.5v3M10 0.5v3" stroke="#333" stroke-width="1.2"/></svg>1 Jan, 2024</span></div></article>
<article class="post" style="left:765px"><div class="post-img" style="background:linear-gradient(180deg,#a9563e 0%,#a9563e 30%,#dcd8d0 30%,#b9b5ae 70%,#4a4a4a 100%)" role="img" aria-label="Open office with people at desks"><span class="tag">Design</span></div><h3>Auto-replay : How to use automated responses</h3><div class="meta"><span><svg width="13" height="13" viewBox="0 0 14 14"><circle cx="7" cy="4.5" r="3" fill="none" stroke="#333" stroke-width="1.2"/><path d="M1.5 13c0-3 2.5-5 5.5-5s5.5 2 5.5 5" fill="none" stroke="#333" stroke-width="1.2"/></svg>by admin</span><span><svg width="13" height="13" viewBox="0 0 14 14"><rect x="1" y="2" width="12" height="11" rx="1" fill="none" stroke="#333" stroke-width="1.2"/><path d="M1 5.5h12M4 0.5v3M10 0.5v3" stroke="#333" stroke-width="1.2"/></svg>1 Jan, 2024</span></div></article>
<div class="btn-fill" style="left:544px;top:3655px;width:111px;height:34px">VIEW ALL</div>

<h2 class="section-title" style="top:3770px">Our Clients</h2>
<div class="client" style="left:160px"><i></i>Brickfield</div>
<div class="client" style="left:378px">Northgate</div>
<div class="client" style="left:550px"><i></i>Corbel</div>
<div class="client" style="left:735px">Keystone</div>
<div class="client" style="left:905px"><i></i>Ironvale</div>

<section class="contact">
  <h2>Talk to a human!</h2>
  <p>Please share some quick info and we'll reach out:</p>
  <div class="field" style="left:68px;top:149px">Name</div>
  <div class="field" style="left:466px;top:149px">Email</div>
  <div class="field" style="left:68px;top:202px">Type of work interested in</div>
  <div class="field" style="left:466px;top:202px">Phone</div>
  <div class="submit">SUBMIT</div>
</section>

<footer class="footer">
  <div class="brand" style="left:140px;top:70px"><span class="brand-dot"></span><span class="brand-name" style="font-size:44px">Toucan</span></div>
  <div class="socials"><i></i><i></i><i></i><i></i></div>
  <div class="fcol" style="left:490px"><h4>Quick Links</h4>Home<br>How it works<br>Blog</div>
  <div class="fcol" style="left:660px"><h4>About</h4>Privacy Policy<br>Terms of Service</div>
  <div class="fcol" style="left:851px"><h4>Contact Info</h4>
    <div class="fcontact"><svg width="14" height="18" viewBox="0 0 14 18"><path d="M7 0a7 7 0 0 0-7 7c0 5 7 11 7 11s7-6 7-11a7 7 0 0 0-7-7zm0 10a3 3 0 1 1 0-6 3 3 0 0 1 0 6z" fill="#b5d22a"/></svg><span>2217 Maple Hollow Ln.<br>Denton, TX 76201</span></div>
    <div class="fcontact"><svg width="16" height="12" viewBox="0 0 16 12"><rect width="16" height="12" rx="1" fill="#b5d22a"/><path d="M0 1l8 6 8-6" stroke="#2f2f2b" stroke-width="1.3" fill="none"/></svg><span>hello@hiketoucan.net</span></div>
    <div class="fcontact"><svg width="14" height="14" viewBox="0 0 24 24"><path fill="#b5d22a" d="M6.6 10.8a15 15 0 0 0 6.6 6.6l2.2-2.2c.3-.3.7-.4 1-.2 1.1.4 2.3.6 3.6.6.6 0 1 .4 1 1V20c0 .6-.4 1-1 1A17 17 0 0 1 3 4c0-.6.4-1 1-1h3.5c.6 0 1 .4 1 1 0 1.3.2 2.5.6 3.6.1.3 0 .7-.2 1z"/></svg><span>555-014-2290</span></div>
  </div>
  <div class="copyright">© 2024 Hiketoucan. All rights reserved.</div>
</footer>

</body>
</html>
```